new business card design - modern, professional, bold, B2B focus - with QR code pls

we are looking for a modern looking, colorful, business card design. some highlights:
- put space for QR code please. probably on the back but I'm open.
- biz card to be orientated VERTICAL not the traditional horizontal.
- do NOT use our full name on the card (ie: Allied Furnace Servicing Inc). Use only AFS Inc or AFS.
- use black and orange with some white. ideally black card with orange and white for the letters/logo etc. gray ok too - for outlines etc.
- we work in HEAVY industrial, so the cards should lend itself to this. our website is alfurnace.example, so you can see what we do.
- do NOT put in little smoke stack pictures / silouettes etc.
- think MODERN and INDUSTRIAL, with a techy focus.

Industry/Entity Type

heavy industrial - all of them. we perform maintenance and inspection services at heavy industrial and commercial businesses. so B2B

Contact Information for Business Card

name, title, phone numbers (cell + hardline), website, email address. of course our logo too - either on front or front and back.

Font styles to use
Other font styles liked:
• montserrat

Colors
F0912C
F2A743
F7CA91
FBE8D2
FDF5EE

Requirements
Must have
• see description
Nice to have
• see description
Should not have
• see description

```html
<!DOCTYPE html>
<html lang="en">
<head>
<meta charset="utf-8">
<title>AFS Inc — Business Card</title>
<link rel="stylesheet" href="https://fonts.googleapis.com/css2?family=Montserrat:wght@400;500;700&display=swap">
<style>
  :root {
    --stage: #3a3a3a;
    --card: #161616;
    --orange: #f7981e;
    --white: #ffffff;
    --grey: #c5beb8;
  }
  html, body {
    margin: 0;
    width: 1200px;
    height: 1200px;
    overflow: hidden;
    background: var(--stage);
    font-family: "Montserrat", sans-serif;
  }
  .stage {
    position: relative;
    width: 1200px;
    height: 1200px;
  }
  .card {
    position: absolute;
    top: 230px;
    width: 420px;
    height: 720px;
    background: var(--card);
    border-radius: 34px;
    box-shadow: 0 3px 0 var(--orange), 0 18px 40px rgba(0,0,0,.45);
    box-sizing: border-box;
  }
  .card--front { left: 150px; }
  .card--back { left: 630px; }

  .wordmark {
    display: flex;
    align-items: center;
    justify-content: center;
    gap: 14px;
    font-weight: 700;
    color: var(--orange);
    letter-spacing: 2px;
  }
  .wordmark__square {
    background: var(--orange);
  }
  .card--front .wordmark {
    position: absolute;
    left: 0; right: 0;
    top: 300px;
    font-size: 110px;
    line-height: 1;
  }
  .card--front .wordmark__square { width: 26px; height: 26px; }

  .card--back .wordmark {
    position: absolute;
    left: 0; right: 0;
    top: 100px;
    font-size: 84px;
    line-height: 1;
  }
  .card--back .wordmark__square { width: 20px; height: 20px; }

  .contact {
    position: absolute;
    left: 70px;
    top: 300px;
    right: 30px;
  }
  .contact__name {
    margin: 0;
    font-size: 34px;
    font-weight: 700;
    color: var(--orange);
    letter-spacing: 1px;
    line-height: 1.05;
  }
  .contact__title {
    margin: 2px 0 22px;
    font-size: 20px;
    font-weight: 400;
    color: var(--white);
    letter-spacing: 1px;
  }
  .contact__list {
    list-style: none;
    margin: 0;
    padding: 0;
  }
  .contact__item {
    display: flex;
    align-items: center;
    gap: 12px;
    font-size: 17px;
    color: var(--white);
    margin-bottom: 10px;
  }
  .contact__icon {
    width: 20px;
    height: 20px;
    flex: none;
  }

  .qr-space {
    position: absolute;
    left: 70px;
    top: 560px;
    width: 110px;
    height: 110px;
    box-sizing: border-box;
    border: 2px dashed var(--orange);
    border-radius: 6px;
    background: rgba(255,255,255,.04);
  }
</style>
</head>
<body>
<main class="stage">

  <section class="card card--front" aria-label="Card front">
    <div class="wordmark">
      <span class="wordmark__square"></span>
      <span class="wordmark__text">AFS</span>
    </div>
  </section>

  <section class="card card--back" aria-label="Card back">
    <div class="wordmark">
      <span class="wordmark__square"></span>
      <span class="wordmark__text">AFS</span>
    </div>

    <div class="contact">
      <h1 class="contact__name">FULL NAME</h1>
      <p class="contact__title">TITLE</p>
      <ul class="contact__list">
        <li class="contact__item">
          <svg class="contact__icon" viewBox="0 0 20 20" aria-hidden="true">
            <rect x="5" y="1.5" width="10" height="17" rx="2" fill="none" stroke="#f7981e" stroke-width="1.6"/>
            <circle cx="10" cy="15.5" r="1" fill="#f7981e"/>
          </svg>
          <span>555-014-2290</span>
        </li>
        <li class="contact__item">
          <svg class="contact__icon" viewBox="0 0 20 20" aria-hidden="true">
            <path d="M4 2.5l3 .5 1.3 3.6-2 1.5c1 2.3 2.8 4.1 5.1 5.1l1.5-2 3.6 1.3.5 3c-.3 1.2-1.4 2-2.7 2C8.5 17.5 2.5 11.5 2.5 5.2c0-1.3.8-2.4 1.5-2.7z" fill="#f7981e"/>
          </svg>
          <span>800-555-0199</span>
        </li>
        <li class="contact__item">
          <svg class="contact__icon" viewBox="0 0 20 20" aria-hidden="true">
            <g fill="none" stroke="#f7981e" stroke-width="1.4">
              <circle cx="10" cy="10" r="8"/>
              <ellipse cx="10" cy="10" rx="3.5" ry="8"/>
              <path d="M2 10h16M3.5 5.5h13M3.5 14.5h13"/>
            </g>
          </svg>
          <span>www.alfurnace.example</span>
        </li>
        <li class="contact__item">
          <svg class="contact__icon" viewBox="0 0 20 20" aria-hidden="true">
            <rect x="1.5" y="4" width="17" height="12" fill="#f7981e"/>
            <path d="M1.5 4l8.5 7 8.5-7M1.5 16l6-5.5M18.5 16l-6-5.5" fill="none" stroke="#161616" stroke-width="1.2"/>
          </svg>
          <span>afsinc@alfurnace.example</span>
        </li>
      </ul>
    </div>

    <div class="qr-space" role="img" aria-label="Space reserved for QR code"></div>
  </section>

</main>
</body>
</html>
```